Need simple and modern looking business card with all my information on one side and logo on the other side
Info :
Company name - VELMAR CONSTRUCTION LLC
Company addres- 418 harbor 87th. Dunmoor park ny 10352
Email- velmarllc@tridomail.Com
Company phone number 555-318-6094
Cell number- 555-742-0583
Web site - velmarllc.Com
My name Gerald tomasino

Target Market(s)

Construction , home improvement, remodeling

Industry/Entity Type

Construction

Contact Information for Business Card

It has to be moder but at the same time simple

Font styles to use
Sans Serif

Colors
0255a3
ffffff
000000
f78f20
b1b1b1
9d9d9d
1b1b1b
33a6d7
ec1f27

Requirements
Must have
• My logo on one side maybe with a some kind of background on the other side all my information
Nice to have
• Some kind of background pictures provided by you .PLEASE HAVE ACCOUNT WITH PIXELVAULT WILL NOT PAY ANY EXTRA FEES .
Should not have
• Any kind of hamer, nails,screws, helmets itp. Please do not copy the other designs come up with something new.

```html
<!DOCTYPE html>
<html lang="en">
<head>
<meta charset="utf-8">
<title>Velmar Construction LLC – Business Card</title>
<link rel="stylesheet" href="https://fonts.googleapis.com/css2?family=Orbitron:wght@500;700&family=Arimo:wght@400&display=swap">
<style>
  :root {
    --card-white: #ffffff;
    --ink-black: #000000;
    --accent-orange: #f39a1f;
    --mark-grey: #b1b1b1;
    --band-grey: #54565a;
    --band-shadow: #3f4145;
  }
  html, body {
    margin: 0;
    padding: 0;
    width: 1200px;
    height: 720px;
    overflow: hidden;
    background: var(--card-white);
  }
  .business-card {
    display: block;
    width: 1200px;
    height: 720px;
  }
  .brand-name {
    font-family: "Orbitron", sans-serif;
    font-weight: 700;
    fill: var(--ink-black);
  }
  .brand-descriptor {
    font-family: "Orbitron", sans-serif;
    font-weight: 500;
    fill: var(--ink-black);
  }
  .brand-mark { fill: var(--mark-grey); }
  .address-line {
    font-family: "Arimo", sans-serif;
    font-weight: 400;
    font-size: 46px;
    fill: var(--card-white);
  }
  .footer-band { fill: var(--band-grey); }
  .footer-band-edge { fill: var(--band-shadow); }
  .footer-swoosh { fill: var(--accent-orange); }
</style>
</head>
<body>
<svg class="business-card" viewBox="0 0 1200 720" xmlns="http://www.w3.org/2000/svg">
  <rect class="card-background" width="1200" height="720" fill="var(--card-white)"/>

  <g class="brand-lockup">
    <rect class="brand-mark" x="768" y="36" width="286" height="284" role="img" aria-label="Company logo mark"/>
    <text class="brand-name" x="128" y="464" font-size="190" textLength="938" lengthAdjust="spacingAndGlyphs">VELMAR</text>
    <text class="brand-descriptor" x="126" y="525" font-size="62" textLength="941" lengthAdjust="spacingAndGlyphs">CONSTRUCTION LLC</text>
  </g>

  <g class="footer">
    <path class="footer-swoosh" d="M0,552 Q420,634 1200,540 L1200,556 Q420,648 0,572 Z"/>
    <path class="footer-band-edge" d="M0,572 Q420,648 1200,556 L1200,564 Q420,656 0,580 Z"/>
    <path class="footer-band" d="M0,578 Q420,654 1200,562 L1200,720 L0,720 Z"/>
    <text class="address-line" x="123" y="700" textLength="1012" lengthAdjust="spacingAndGlyphs">418 harbor 87th. Dunmoor park ny 10352</text>
  </g>
</svg>
</body>
</html>
```